Stationery Design Project

Would like to have the design elements we created in for our website (www.brook-holdings.example), incorporated in a stationery design layout.
Updates
Colors used in the logo attachments do not need to be used. We are open to different color variations. Looking for a crisp, clean, modern update using the design elements in attachments and which can also be viewed on or website.
A note to designers:
Project Deadline Extended
Reason: Due to update in our project description and requirements, we have decided to extend the deadline of this project to provide ample opportunity to all designers participating .
Requirements
Must have
- Must have continuity with the theme and design features used in our website. Have attached .jpg images of some of the design elements.

```html
<!DOCTYPE html>
<html lang="en">
<head>
<meta charset="utf-8">
<title>Brook Holdings Letterhead</title>
<link href="https://fonts.googleapis.com/css2?family=Sorts+Mill+Goudy&display=swap" rel="stylesheet">
<style>
  :root {
    --paper: #ffffff;
    --ink: #1a1a1a;
    --band-green: #6e8038;
    --band-mid: #3e4a22;
    --band-dark: #050505;
    --logo-ink: #ffffff;
  }
  html, body {
    margin: 0;
    padding: 0;
    overflow: hidden;
    background: var(--paper);
  }
  .letterhead {
    position: relative;
    width: 939px;
    height: 1200px;
    overflow: hidden;
    background: var(--paper);
    color: var(--ink);
    font-family: "Sorts Mill Goudy", Georgia, serif;
  }
  .header-band {
    position: absolute;
    left: 0;
    top: 0;
    width: 910px;
    height: 182px;
    background: linear-gradient(90deg, var(--band-green) 0%, var(--band-green) 25%, var(--band-mid) 65%, var(--band-dark) 100%);
  }
  .brand-name {
    position: absolute;
    left: 72px;
    top: 68px;
    margin: 0;
    font-size: 56px;
    font-weight: 400;
    line-height: 1;
    color: var(--logo-ink);
  }
  .sender-address {
    position: absolute;
    left: 69px;
    top: 202px;
    font-style: normal;
    font-size: 15px;
    line-height: 15px;
  }
  .letter-body {
    position: absolute;
    left: 69px;
    top: 381px;
    width: 801px;
    font-size: 14.4px;
    line-height: 17.6px;
  }
  .salutation {
    margin: 0 0 17.6px;
  }
  .letter-body .paragraph {
    margin: 0 0 17.6px;
    text-indent: 40px;
    text-align: justify;
    hyphens: auto;
  }
  .closing {
    position: absolute;
    left: 592px;
    top: 922px;
    font-size: 14.4px;
    line-height: 22px;
  }
  .footer-contact {
    position: absolute;
    left: 0;
    width: 939px;
    top: 1098px;
    text-align: center;
    font-size: 14.4px;
    line-height: 22px;
  }
</style>
</head>
<body>
  <div class="letterhead">
    <header class="header-band">
      <h1 class="brand-name">Brook</h1>
    </header>

    <address class="sender-address">
      418 Alder Creek Road Suite 102<br>
      Millford, GA 30999<br>
      PHONE: (555) 014-2290<br>
      FAX: (555) 014-2291
    </address>

    <main class="letter-body">
      <p class="salutation">Dear To Whome This May Interest,</p>
      <p class="paragraph">Lorem ipsum dolor sit amet, consectetuer adipiscing elit. Nullam ornare dictum ligula. Maecenas elementum suscipit nisl. Cras imperdiet leo ac felis dictum luctus. Pellentesque odio nisi, accumsan nec, scelerisque sed, consectetuer nec, justo. Sed tortor sapien, suscipit id, pulvinar vel, elementum id, lorem. Nullam consectetuer risus sit amet nibh. Vestibulum consectetuer, quam vitae euismod volutpat, magna magna consectetuer dui, et accumsan magna dui non nibh. Morbi adipiscing consequat erat. Vivamus quis massa eget orci fermentum laoreet. Morbi posuere purus. Duis feugiat lacus vel nisi. Aliquam ipsum felis, pretium sed, vehicula vel, dictum eget, nibh. Morbi turpis nulla, luctus viverra, pretium in, suscipit vitae, purus.</p>
      <p class="paragraph">Morbi gravida lacus sed lorem. Mauris vestibulum. Cras vehicula porta eros. Curabitur ut justo vel pede elementum semper. Integer pretium pulvinar augue. Aenean ut nisl non lectus porta feugiat. Mauris iaculis pede a risus. Suspendisse mollis. Donec suscipit. Sed tellus magna, tempus a, ultricies in, dignissim et, nulla. Pellentesque habitant morbi tristique senectus et netus et malesuada fames ac turpis egestas. Suspendisse potenti. Proin viverra vulputate pede. Sed nec mauris ut turpis convallis tempus. Maecenas id justo vitae lacus fringilla interdum. Nulla diam.</p>
      <p class="paragraph">Phasellus interdum dictum tellus. Donec convallis leo in orci. Vestibulum eget nibh. Nullam consectetuer blandit elit. Cras non ipsum ut nulla pulvinar consequat. Maecenas tincidunt, dui sed interdum vehicula, justo arcu tempus risus, id semper arcu velit sit amet mi. Donec sem. Sed pulvinar fringilla elit. Quisque ante. Cras tempor lobortis velit. Phasellus porta arcu sit amet libero. Aenean aliquet, leo in porta aliquam, est tortor accumsan justo, vel ultrices leo dui nec velit. Etiam vel nibh. Quisque eu ante ut diam auctor molestie. Nullam mattis, nulla et molestie cursus, neque orci consectetuer nisl, eget consequat sapien pede vitae augue. Fusce pretium velit et lacus. Cras commodo sagittis velit. Proin lobortis, diam in semper viverra, enim pede adipiscing massa, a convallis enim sem consectetuer odio.</p>
    </main>

    <div class="closing">
      Sincerely,<br>
      Brook Holdings
    </div>

    <footer class="footer-contact">
      www.brook-holdings.example<br>
      info@brook-holdings.example
    </footer>
  </div>
</body>
</html>
```